RivoPlex PowerPoint Template with existing Logo and Letterhead template

Develop a PowerPoint template based on existing logo and letterhead designs for a Marketing Consultancy.
Presentations that will be made with title slide, content slides (which includes mostly bullet point text and some tables) and also last page company introduction and copyright.
Corporate colors should be keep as per the logo

I like something like from Artisan Hive
- Serious, Modern PowerPoint Design for Company in Canada | Design 418674
- Professional, Modern PowerPoint Design for Company in United States | Design 7795293
- Professional, Modern PowerPoint Design for Company in United States | Design 7826742
- Serious, Modern PowerPoint Design for Company in Canada | Design 418635
- Elegant, Serious PowerPoint Design for Company in Puerto Rico | Design 16951178
- Bold, Modern PowerPoint Design for Company in United States | Design 11745238

To all designers, • We need sleek and modern looking PowerPoint presentation template. • The template will primarily be used for our corporate slide and solutions presentation for our customers. • Not too much of white and it should be sleek, modern and impressive for marketing consultancy firms like us. • Please ensure the content pages are water marketed with the 4 boxes. • I like something like from Artisan Hive and you can get some idea on what I like.: o Serious, Modern PowerPoint Design for Company in Canada | Design 418674 o Professional, Modern PowerPoint Design for Company in United States | Design 7795293 o Professional, Modern PowerPoint Design for Company in United States | Design 7826742 o Serious, Modern PowerPoint Design for Company in Canada | Design 418635 o Elegant, Serious PowerPoint Design for Company in Puerto Rico | Design 16951178 o Bold, Modern PowerPoint Design for Company in United States | Design 11745238 Thanks!

Target Market(s)

Marketing Managers, B2B Marketing Team, CRM Data Owners

Industry/Entity Type

Marketing

Requirements
Must have
• Not too much of white and it should be sleek, modern and impressive for marketing consultancy firms like us. Please ensure the content pages are water marketed with the 4 boxes. The template will primarily be used for our corporate slides and solutions presentation for our customers.
Should not have
• no background in the slide content area

```html
<!DOCTYPE html>
<html lang="en">
<head>
<meta charset="utf-8">
<title>RivoPlex Presentation Template</title>
<link rel="stylesheet" href="https://fonts.googleapis.com/css2?family=Open+Sans:wght@400;600;700&family=Roboto:wght@400&display=swap">
<style>
:root{
  --red:#e52127;
  --red-dark:#a8121a;
  --slate:#5b6579;
  --slate-light:#8a93a3;
  --ink:#3f4552;
  --mist:#ececee;
  --paper:#ffffff;
  --page:#ffffff;
}
*{margin:0;padding:0;box-sizing:border-box}
html,body{width:1200px;height:1200px;overflow:hidden;background:var(--page)}
body{position:relative;font-family:"Open Sans",sans-serif;color:var(--ink)}
.slide-frame{position:absolute;width:553px;height:312px;box-shadow:0 1px 4px rgba(0,0,0,.28);overflow:hidden}
.slide{position:absolute;left:0;top:0;width:691px;height:390px;transform:scale(.8);transform-origin:0 0;background:var(--paper);overflow:hidden}
.slide *{position:absolute}
.caption{position:absolute;width:400px;margin-left:-200px;text-align:center;font-family:"Roboto",sans-serif;font-size:16px;color:#222;letter-spacing:.2px}
.brand{font-weight:700;color:var(--red);letter-spacing:2px;white-space:nowrap}
.brand-mark{background:var(--slate)}
.headline{font-weight:600;line-height:1.15;white-space:nowrap}
.headline .hl{color:var(--red)}
.rule{height:2px;background:var(--slate)}
.footer-band{height:18px;background:var(--slate);left:0;top:350px}
.footer-url{font-size:6.5px;color:#fff;letter-spacing:2px;top:355px;white-space:nowrap}
.footer-line{height:1px;background:#fff;top:359px}
.page-num{font-size:6px;color:var(--ink);top:356px}
.tiny{font-size:7px;line-height:1.45;color:var(--ink)}
.photo{display:block}
</style>
</head>
<body>

<!-- Cover -->
<div class="slide-frame" style="left:29px;top:50px">
  <div class="slide cover">
    <svg style="left:0;top:0" width="691" height="390" viewBox="0 0 691 390">
      <defs>
        <linearGradient id="night" x1="0" y1="0" x2="0" y2="1">
          <stop offset="0" stop-color="#3b3f9a"/>
          <stop offset=".55" stop-color="#26307a"/>
          <stop offset="1" stop-color="#151b3e"/>
        </linearGradient>
      </defs>
      <polygon points="0,0 120,0 196,122 0,122" fill="var(--red-dark)"/>
      <polygon points="186,104 691,104 691,121 197,121" fill="var(--red-dark)"/>
      <polygon points="0,122 196,122 278,254 0,254" fill="var(--slate)"/>
      <polygon points="304,290 691,290 691,390 356,390" fill="var(--slate)"/>
      <polygon points="276,254 304,290 330,345 296,345" fill="var(--red-dark)"/>
      <polygon points="120,0 138,0 334,345 314,345" fill="var(--red)"/>
      <line x1="398" y1="363" x2="575" y2="363" stroke="#fff" stroke-width=".6"/>
    </svg>
    <svg class="photo" role="img" aria-label="Night city skyline over water" style="left:0;top:0" width="691" height="390" viewBox="0 0 691 390">
      <polygon points="198,122 691,122 691,290 304,290" fill="url(#night)"/>
    </svg>
    <div class="brand" style="left:318px;top:52px;font-size:26px">RIVOPLEX</div>
    <div class="brand-mark" style="left:508px;top:30px;width:10px;height:10px;background:var(--red)"></div>
    <div style="left:20px;top:178px;font-size:8.5px;color:#fff;font-weight:600">INBOUND &amp; OUTBOUND CALL CENTRES</div>
    <div style="left:20px;top:193px;font-size:5.5px;line-height:1.5;color:#fff">Attract new leads, increase sales and inspire customers<br>through our in-country call centres network</div>
    <div style="left:20px;top:291px;font-size:19px;color:var(--slate);line-height:1.2">LOREM IPSUM IS<br>SIMPLY <span style="position:static;color:var(--red)">DUMMY TEXT</span></div>
    <div style="left:20px;top:340px;width:197px;height:13px;background:var(--slate);color:#fff;font-size:7px;letter-spacing:1.5px;padding:2px 4px;white-space:nowrap">2018 LOREM IPSUM IS SIMPLY DUMMY</div>
    <div style="left:580px;top:359px;font-size:6.5px;color:#fff;letter-spacing:1.5px">www.rivoplex.com</div>
  </div>
</div>
<div class="caption" style="left:305px;top:380px">COVER PAGE</div>

<!-- Inner page 01 -->
<div class="slide-frame" style="left:621px;top:50px">
  <div class="slide">
    <div class="headline" style="left:19px;top:14px;font-size:31px;color:var(--slate)">LOREM <span class="hl" style="position:static">IPSUM TEXT</span></div>
    <div class="rule" style="left:19px;top:55px;width:94px"></div>
    <div class="brand" style="left:588px;top:30px;font-size:11px;letter-spacing:1px">RIVOPLEX</div>
    <svg style="left:0;top:0" width="691" height="390" viewBox="0 0 691 390">
      <g fill="none" stroke-width="7">
        <circle cx="92" cy="138" r="45" stroke="var(--red)" stroke-dasharray="141 283" transform="rotate(180 92 138)"/>
        <circle cx="486" cy="138" r="45" stroke="var(--red-dark)" stroke-dasharray="198 283" transform="rotate(180 486 138)"/>
        <circle cx="92" cy="284" r="45" stroke="var(--slate)" stroke-dasharray="90 283" transform="rotate(180 92 284)"/>
        <circle cx="486" cy="284" r="45" stroke="#1b1b1b" stroke-dasharray="62 283" transform="rotate(205 486 284)"/>
      </g>
      <g fill="var(--mist)">
        <circle cx="92" cy="138" r="40"/><circle cx="486" cy="138" r="40"/>
        <circle cx="92" cy="284" r="40"/><circle cx="486" cy="284" r="40"/>
      </g>
      <line x1="355" y1="135" x2="355" y2="310" stroke="#e4e4e6" stroke-width="1"/>
    </svg>
    <div style="left:72px;top:126px;width:40px;text-align:center;font-size:19px;font-weight:600">50</div>
    <div style="left:466px;top:126px;width:40px;text-align:center;font-size:19px;font-weight:600">70</div>
    <div style="left:72px;top:272px;width:40px;text-align:center;font-size:19px;font-weight:600">30</div>
    <div style="left:466px;top:272px;width:40px;text-align:center;font-size:19px;font-weight:600">10</div>
    <div style="left:152px;top:116px"><div style="position:static;font-size:10px">lorem ipsum simply</div><div class="tiny" style="position:static;font-size:6.5px">Lorem Ipsum is simply<br>dummy text of the printing<br>and typesetting industry.</div></div>
    <div style="left:545px;top:116px"><div style="position:static;font-size:10px">lorem ipsum simply</div><div class="tiny" style="position:static;font-size:6.5px">Lorem Ipsum is simply<br>dummy text of the printing<br>and typesetting industry.</div></div>
    <div style="left:152px;top:262px"><div style="position:static;font-size:10px">lorem ipsum simply</div><div class="tiny" style="position:static;font-size:6.5px">Lorem Ipsum is simply<br>dummy text of the printing<br>and typesetting industry.</div></div>
    <div style="left:545px;top:262px"><div style="position:static;font-size:10px">lorem ipsum simply</div><div class="tiny" style="position:static;font-size:6.5px">Lorem Ipsum is simply<br>dummy text of the printing<br>and typesetting industry.</div></div>
    <div class="footer-band" style="width:628px"></div>
    <div class="footer-line" style="left:254px;width:48px"></div>
    <div class="footer-url" style="left:305px">www.rivoplex.com</div>
    <div class="footer-line" style="left:392px;width:48px"></div>
    <div class="page-num" style="left:662px">01</div>
  </div>
</div>
<div class="caption" style="left:897px;top:380px">INNER PAGE 01</div>

<!-- Inner page 02 -->
<div class="slide-frame" style="left:29px;top:424px">
  <div class="slide">
    <div class="headline" style="left:19px;top:64px;font-size:31px;color:var(--slate)">LOREM</div>
    <div class="headline" style="left:19px;top:104px;font-size:31px;color:var(--red)">IPSUM TEXT</div>
    <div class="tiny" style="left:20px;top:164px;width:215px;font-size:8.4px;line-height:1.62;text-align:justify"><span style="position:static;color:var(--red)">Lorem Ipsum is simply dummy</span> text of the printing and typesetting industry. Lorem Ipsum has been the industry's standard dummy text ever since the 1500s, when an unknown printer took a galley of type and scrambled it to make a type specimen book. It has survived not only five centuries. But also the leap into electronic typesetting, remaining essentially unchanged. It was popularised in the 1960s with the release of Letraset sheets containing.</div>
    <svg class="photo" role="img" aria-label="Blue notebook and tablet on a wooden desk" style="left:280px;top:0" width="256" height="324" viewBox="0 0 256 324">
      <defs>
        <linearGradient id="desk" x1="0" y1="0" x2="1" y2="1">
          <stop offset="0" stop-color="#d9b98e"/>
          <stop offset=".45" stop-color="#2a45b8"/>
          <stop offset=".7" stop-color="#c8a57a"/>
          <stop offset="1" stop-color="#e0c49c"/>
        </linearGradient>
      </defs>
      <path d="M0 0H256V314a10 10 0 0 1-10 10H10A10 10 0 0 1 0 314Z" fill="url(#desk)"/>
    </svg>
    <div style="left:467px;top:158px;width:203px;height:125px;background:#fff;border:1px solid #cfd2d8;border-radius:10px"></div>
    <div style="left:480px;top:174px;font-size:12px;color:var(--red)">LOREM IPSUM</div>
    <div class="tiny" style="left:480px;top:199px;width:177px;font-size:8px;line-height:1.65;text-align:justify"><span style="position:static;color:var(--red)">Lorem Ipsum is simply dummy</span> text of the printing and typesetting industry. Lorem Ipsum has been the industry's standard dummy text ever since the 1500s, when an unknown printer took a galley of type.</div>
    <div class="brand" style="left:588px;top:30px;font-size:11px;letter-spacing:1px">RIVOPLEX</div>
    <div class="footer-band" style="width:290px"></div>
    <div class="footer-line" style="left:48px;width:46px"></div>
    <div class="footer-url" style="left:100px">www.rivoplex.com</div>
    <div class="footer-line" style="left:186px;width:46px"></div>
    <div class="page-num" style="left:662px">02</div>
  </div>
</div>
<div class="caption" style="left:305px;top:756px">INNER PAGE 02</div>

<!-- Inner page 03 -->
<div class="slide-frame" style="left:621px;top:424px">
  <div class="slide">
    <svg class="photo" role="img" aria-label="Hand writing with a pen at a desk" style="left:36px;top:0" width="214" height="321" viewBox="0 0 214 321">
      <defs>
        <linearGradient id="desk2" x1="0" y1="0" x2="0" y2="1">
          <stop offset="0" stop-color="#7d8798"/>
          <stop offset=".5" stop-color="#6b7487"/>
          <stop offset="1" stop-color="#565f72"/>
        </linearGradient>
      </defs>
      <path d="M0 0H214V311a10 10 0 0 1-10 10H10A10 10 0 0 1 0 311Z" fill="url(#desk2)"/>
    </svg>
    <div style="left:36px;top:205px;width:214px;text-align:center;color:#fff;font-weight:700;font-size:24px;line-height:1.4">LOREM IPSUM<br>SIMPLY TEXT<br>TYPESETTING</div>
    <div class="brand" style="left:588px;top:30px;font-size:11px;letter-spacing:1px">RIVOPLEX</div>
    <svg style="left:0;top:0" width="691" height="390" viewBox="0 0 691 390">
      <circle cx="453" cy="182" r="88" fill="#f2f2f3"/>
      <circle cx="453" cy="182" r="70" fill="#fff" stroke="#e6e6e8" stroke-width="3"/>
      <rect x="443" y="172" width="20" height="20" fill="var(--red)"/>
      <g fill="none" stroke="var(--slate-light)" stroke-width=".8">
        <polyline points="358,97 405,97 405,120 416,120"/>
        <polyline points="358,175 375,175"/>
        <polyline points="358,255 390,255 390,230 400,230"/>
        <polyline points="567,97 518,97 518,120 507,120"/>
        <polyline points="567,175 550,175"/>
        <polyline points="567,255 526,255 526,230 516,230"/>
      </g>
      <g fill="var(--slate-light)">
        <circle cx="358" cy="97" r="1.6"/><circle cx="358" cy="175" r="1.6"/><circle cx="358" cy="255" r="1.6"/>
        <circle cx="567" cy="97" r="1.6"/><circle cx="567" cy="175" r="1.6"/><circle cx="567" cy="255" r="1.6"/>
      </g>
    </svg>
    <div class="tiny" style="left:262px;top:93px;width:90px;text-align:right;font-size:6.6px"><span style="position:static;color:var(--red);font-weight:600">STEP 01</span><br>Lorem Ipsum is simply<br>dummy text of the.</div>
    <div class="tiny" style="left:262px;top:171px;width:90px;text-align:right;font-size:6.6px"><span style="position:static;color:var(--red);font-weight:600">STEP 02</span><br>Lorem Ipsum is simply<br>dummy text of the.</div>
    <div class="tiny" style="left:262px;top:250px;width:90px;text-align:right;font-size:6.6px"><span style="position:static;color:var(--red);font-weight:600">STEP 03</span><br>Lorem Ipsum is simply<br>dummy text of the.</div>
    <div class="tiny" style="left:573px;top:93px;width:90px;font-size:6.6px"><span style="position:static;color:var(--red);font-weight:600">STEP 04</span><br>Lorem Ipsum is simply<br>dummy text of the.</div>
    <div class="tiny" style="left:573px;top:171px;width:90px;font-size:6.6px"><span style="position:static;color:var(--red);font-weight:600">STEP 05</span><br>Lorem Ipsum is simply<br>dummy text of the.</div>
    <div class="tiny" style="left:573px;top:250px;width:90px;font-size:6.6px"><span style="position:static;color:var(--red);font-weight:600">STEP 06</span><br>Lorem Ipsum is simply<br>dummy text of the.</div>
    <div class="footer-band" style="width:290px"></div>
    <div class="footer-line" style="left:48px;width:46px"></div>
    <div class="footer-url" style="left:100px">www.rivoplex.com</div>
    <div class="footer-line" style="left:186px;width:46px"></div>
    <div class="page-num" style="left:662px">03</div>
  </div>
</div>
<div class="caption" style="left:897px;top:756px">INNER PAGE 03</div>

<!-- Inner page 04: timeline -->
<div class="slide-frame" style="left:29px;top:808px">
  <div class="slide">
    <div class="headline" style="left:19px;top:30px;font-size:31px;color:var(--slate)">LOREM</div>
    <div class="headline" style="left:19px;top:70px;font-size:31px;color:var(--red)">IPSUM TEXT</div>
    <div class="rule" style="left:19px;top:111px;width:94px"></div>
    <div class="brand" style="left:588px;top:30px;font-size:11px;letter-spacing:1px">RIVOPLEX</div>
    <svg style="left:0;top:0" width="691" height="390" viewBox="0 0 691 390">
      <rect x="70" y="216" width="138" height="14" fill="var(--slate)"/>
      <rect x="207" y="216" width="140" height="14" fill="var(--slate-light)"/>
      <rect x="346" y="216" width="139" height="14" fill="var(--red)"/>
      <rect x="484" y="216" width="138" height="14" fill="var(--red-dark)"/>
      <circle cx="70" cy="223" r="17" fill="var(--slate)"/>
      <circle cx="207" cy="223" r="17" fill="var(--slate-light)"/>
      <circle cx="346" cy="223" r="17" fill="var(--red)"/>
      <circle cx="484" cy="223" r="17" fill="var(--red)"/>
      <circle cx="622" cy="223" r="17" fill="var(--red-dark)"/>
      <g fill="none" stroke="#fff" stroke-width="1.6">
        <circle cx="66" cy="220" r="4.5"/><circle cx="75" cy="228" r="3"/>
        <rect x="199" y="216" width="16" height="11" rx="1"/><line x1="203" y1="231" x2="211" y2="231"/>
        <circle cx="346" cy="223" r="8"/><circle cx="346" cy="223" r="4"/>
        <rect x="477" y="219" width="14" height="10"/><line x1="481" y1="215" x2="481" y2="219"/><line x1="487" y1="215" x2="487" y2="219"/>
        <ellipse cx="622" cy="223" rx="9" ry="4"/><ellipse cx="622" cy="223" rx="4" ry="9"/>
      </g>
      <polygon points="70,248 65,242 75,242" fill="var(--slate)"/>
      <polygon points="207,192 202,198 212,198" fill="var(--slate-light)"/>
      <polygon points="346,248 341,242 351,242" fill="var(--red)"/>
      <polygon points="484,192 479,198 489,198" fill="var(--red)"/>
      <polygon points="622,248 617,242 627,242" fill="var(--red-dark)"/>
    </svg>
    <div class="tiny" style="left:20px;top:160px;width:110px;font-size:5.6px"><b style="position:static;display:block;padding-left:42px;font-size:6px">TITLE</b>Lorem Ipsum is simply dummy text of the printing and typesetting industry.</div>
    <div class="tiny" style="left:297px;top:160px;width:110px;font-size:5.6px"><b style="position:static;display:block;padding-left:42px;font-size:6px">TITLE</b>Lorem Ipsum is simply dummy text of the printing and typesetting industry.</div>
    <div class="tiny" style="left:572px;top:160px;width:110px;font-size:5.6px"><b style="position:static;display:block;padding-left:42px;font-size:6px">TITLE</b>Lorem Ipsum is simply dummy text of the printing and typesetting industry.</div>
    <div class="tiny" style="left:158px;top:250px;width:110px;font-size:5.6px"><b style="position:static;display:block;padding-left:42px;font-size:6px">TITLE</b>Lorem Ipsum is simply dummy text of the printing and typesetting industry.</div>
    <div class="tiny" style="left:435px;top:250px;width:110px;font-size:5.6px"><b style="position:static;display:block;padding-left:42px;font-size:6px">TITLE</b>Lorem Ipsum is simply dummy text of the printing and typesetting industry.</div>
    <div style="left:60px;top:259px;font-size:4.5px;font-weight:700">STEP 01</div>
    <div style="left:197px;top:179px;font-size:4.5px;font-weight:700">STEP 02</div>
    <div style="left:336px;top:259px;font-size:4.5px;font-weight:700">STEP 03</div>
    <div style="left:474px;top:179px;font-size:4.5px;font-weight:700">STEP 04</div>
    <div style="left:612px;top:259px;font-size:4.5px;font-weight:700">STEP 05</div>
    <div class="footer-band" style="width:290px"></div>
    <div class="footer-line" style="left:48px;width:46px"></div>
    <div class="footer-url" style="left:100px">www.rivoplex.com</div>
    <div class="footer-line" style="left:186px;width:46px"></div>
    <div class="page-num" style="left:662px">04</div>
  </div>
</div>
<div class="caption" style="left:305px;top:1140px">INNER PAGE 04</div>

<!-- Closing page -->
<div class="slide-frame" style="left:621px;top:808px">
  <div class="slide">
    <div class="brand" style="left:232px;top:50px;width:227px;text-align:center;font-size:27px">RIVOPLEX</div>
    <div style="left:441px;top:22px;width:10px;height:10px;background:var(--red)"></div>
    <div style="left:0;top:113px;width:691px;height:117px;background:var(--slate)"></div>
    <div style="left:0;top:134px;width:691px;text-align:center;font-size:15px;color:#fff">LOREM IPSUM IS</div>
    <div style="left:0;top:155px;width:691px;text-align:center;font-size:15px;color:var(--red)">LOREM IPSUM IS SIMPLY</div>
    <div style="left:210px;top:178px;width:271px;height:1px;background:#8c95a6"></div>
    <div style="left:210px;top:192px;width:271px;text-align:center;font-size:6px;line-height:1.6;color:#fff">Lorem Ipsum is simply dummy text of the printing and typesetting industry. Lorem Ipsum has been the industry's standard dummy text ever since the 1500s</div>
    <div style="left:0;top:254px;width:691px;text-align:center;font-size:16px;font-weight:600;white-space:nowrap"><span style="position:static;color:var(--red)">CALL US TODAY</span>&nbsp; <span style="position:static;color:var(--slate)">+1 (555) 014-2270</span></div>
    <div style="left:0;top:284px;width:691px;text-align:center;font-size:6.5px;color:var(--ink)">&#9679; 410 Harbor Lane, Suite 20, Springfield, CA 90001, USA</div>
    <div style="left:0;top:301px;width:691px;text-align:center;font-size:6.5px;color:var(--ink)">&#9993; hello@rivoplex.com</div>
    <div style="left:0;top:318px;width:691px;text-align:center;font-size:6.5px;color:var(--ink)">&#9719; Monday – Friday : 9AM – 6PM</div>
    <div style="left:254px;top:366px;width:46px;height:1px;background:var(--slate-light)"></div>
    <div style="left:305px;top:362px;font-size:6.5px;letter-spacing:2px;color:var(--slate)">www.rivoplex.com</div>
    <div style="left:392px;top:366px;width:46px;height:1px;background:var(--slate-light)"></div>
  </div>
</div>
<div class="caption" style="left:897px;top:1140px">INNER PAGE 04</div>

</body>
</html>
```